QRV Law Letterhead

Want law firm letterhead - both in terms of a pdf file that I can use electronically as letterhead by adding it as a background - and in terms of a file that I can send to a company to create actual letterhead.
Industry/Entity Type
Law Firm
Font styles to use
Sans Serif
Requirements
Must have
- Should have the following information (you can decide where to place):
- My name - Corwin Haldane
- My email - corwin@qrvlawfirm.example
- My address - 2816 Pellworth Parkway 317-842
- Fenwick Bay, Oregon 95742
- Website - www.qrvlawfirm.example
- Phone - 541-555-0187
- Fax - 541-555-0243
- The logo I attached
Nice to have
- I think I would prefer to have a black and white color scheme.
- I don't necessarily need a title after my name, but I have seen a few design submissions that include a generic title. The title I would use is "IP Litigator & Trademark Attorney"

```html
<!DOCTYPE html>
<html lang="en">
<head>
<meta charset="utf-8">
<title>QRV Law Letterhead</title>
<link href="https://fonts.googleapis.com/css2?family=Open+Sans:wght@400;600;700&display=swap" rel="stylesheet">
<style>
  :root {
    --ink: #111111;
    --text: #2a2a2a;
    --muted: #6a6a6a;
    --rule: #c9c9c9;
    --paper: #ffffff;
    --backdrop: #ececec;
    --band: #0b0b0b;
    --signature-tone: #d8d8d8;
  }
  * { box-sizing: border-box; margin: 0; padding: 0; }
  html, body {
    width: 1200px; height: 786px; overflow: hidden;
    background: var(--backdrop);
    font-family: "Open Sans", Arial, sans-serif;
    color: var(--text);
  }
  .letterhead {
    position: absolute; left: 314px; top: 22px;
    width: 572px; height: 742px;
    background: var(--paper);
    box-shadow: 0 2px 10px rgba(0,0,0,0.12);
    display: flex; flex-direction: column;
  }
  .header-band {
    height: 42px; background: var(--band);
    display: flex; align-items: center; justify-content: space-between;
    padding: 0 24px 0 26px; color: var(--paper);
  }
  .brand { display: flex; align-items: center; gap: 9px; }
  .brand-dot {
    width: 24px; height: 24px; border-radius: 50%;
    border: 2px solid var(--paper);
  }
  .brand-name { font-size: 19px; font-weight: 600; letter-spacing: 0.3px; }
  .attorney-name {
    font-size: 7.5px; font-weight: 700; letter-spacing: 1px; text-transform: uppercase;
  }
  .letter-body { padding: 30px 40px 0 44px; flex: 1; }
  .salutation { font-size: 11px; font-weight: 700; color: var(--ink); margin-bottom: 8px; }
  .letter-body p {
    font-size: 8.6px; line-height: 1.5; margin-bottom: 12px; color: var(--text);
  }
  .signature {
    width: 96px; height: 38px; margin: 16px 0 0 118px;
    background: linear-gradient(90deg, var(--signature-tone), #efefef);
    border-radius: 3px;
  }
  .contact-footer {
    display: flex; align-items: flex-end;
    padding: 0 36px 22px 44px;
  }
  .contact-item {
    flex: 1; display: flex; flex-direction: column; align-items: center;
    gap: 8px; font-size: 7.5px; line-height: 1.5; color: var(--muted); text-align: center;
  }
  .contact-item strong { color: var(--ink); font-weight: 700; }
  .contact-item svg { width: 12px; height: 12px; }
  .divider { width: 1px; height: 44px; background: var(--rule); }
  .footer-bar { height: 10px; background: var(--band); }
</style>
</head>
<body>
  <main class="letterhead">
    <header class="header-band">
      <div class="brand">
        <span class="brand-dot"></span>
        <span class="brand-name">QRV Law</span>
      </div>
      <span class="attorney-name">Corwin Haldane</span>
    </header>

    <section class="letter-body">
      <h2 class="salutation">Dear Mr. Ellery,</h2>
      <p>Lorem Ipsum is simply dummy text of the printing and typesetting industry. Lorem Ipsum has been the industry's standard dummy text ever since the 1500s, when an unknown printer took a galley of type and scrambled it to make a type specimen book. It has survived not only five centuries, but also the leap into electronic typesetting, remaining essentially unchanged.</p>
      <p>The standard chunk of Lorem Ipsum used since the 1500s is reproduced below for those interested. Sections 1.10.32 and 1.10.33 from "de Rebus Minimis et Maximis" by Aulus Venn are also reproduced in their exact original form, accompanied by English versions from the 1914 translation by T. Morrell.</p>
      <p>Lorem Ipsum is simply dummy text of the printing and typesetting industry. Lorem Ipsum has been the industry's standard dummy text ever since the 1500s, when an unknown printer took a galley of type and scrambled it to make a type specimen book. It has survived not only five centuries, but also the leap into electronic typesetting, remaining essentially unchanged. It was popularised in the</p>
      <p>The standard chunk of Lorem Ipsum used since the 1500s is reproduced below for those interested. Sections 1.10.32 and 1.10.33 from "de Rebus Minimis et Maximis" by Aulus Venn are also reproduced in their exact original form, accompanied by English versions from the 1914 translation by T. Morrell.</p>
      <p>The standard chunk of Lorem Ipsum used since the 1500s is reproduced below for those interested. Sections 1.10.32 and 1.10.33 from "de Rebus Minimis et Maximis" by Aulus Venn are also reproduced in their exact original form.</p>
      <div class="signature" role="img" aria-label="Handwritten signature of the attorney"></div>
    </section>

    <footer class="contact-footer">
      <div class="contact-item">
        <svg viewBox="0 0 12 12" aria-hidden="true"><path d="M6 0.5a4 4 0 0 1 4 4c0 3-4 7-4 7s-4-4-4-7a4 4 0 0 1 4-4z" fill="var(--ink)"/><circle cx="6" cy="4.5" r="1.5" fill="var(--paper)"/></svg>
        <span>2816 Pellworth Parkway 317-842<br>Fenwick Bay, Oregon 95742</span>
      </div>
      <span class="divider"></span>
      <div class="contact-item">
        <svg viewBox="0 0 12 12" aria-hidden="true"><circle cx="6" cy="6" r="5.3" fill="none" stroke="var(--ink)" stroke-width="1.2"/><path d="M4.2 3.3l1 .1.5 1.4-.8.6a4 4 0 0 0 1.7 1.7l.6-.8 1.4.5.1 1-.9.8C5.6 8.4 3.6 6.4 3.4 4.2z" fill="var(--ink)"/></svg>
        <span><strong>P:</strong> 541-555-0187<br><strong>F:</strong> 541-555-0243</span>
      </div>
      <span class="divider"></span>
      <div class="contact-item">
        <svg viewBox="0 0 12 12" aria-hidden="true"><circle cx="6" cy="6" r="5.3" fill="none" stroke="var(--ink)" stroke-width="1.1"/><ellipse cx="6" cy="6" rx="2.3" ry="5.3" fill="none" stroke="var(--ink)" stroke-width="0.9"/><path d="M0.8 6h10.4" stroke="var(--ink)" stroke-width="0.9"/></svg>
        <span>corwin@qrvlawfirm.example<br>www.qrvlawfirm.example</span>
      </div>
    </footer>
    <div class="footer-bar"></div>
  </main>
</body>
</html>
```